RWTB Core Values

Core Values poster, A fun poster that has a light feel that clearly shows the five values.

Customer 1st, Loyalty, Education, quAlity, Respect.

If it works making the letters that spell out CLEAR jump out a little.

Industry/Entity Type

Education

```html
<!DOCTYPE html>
<html lang="en">
<head>
<meta charset="utf-8">
<title>RWTB Core Values Poster</title>
<link href="https://fonts.googleapis.com/css2?family=Roboto+Condensed:wght@700&family=Tinos:wght@400;700&family=Arimo&display=swap" rel="stylesheet">
<style>
  :root {
    --backdrop: #1e1a19;
    --poster-yellow: #fff200;
    --poster-lime: #c8df14;
    --poster-green: #7ec42a;
    --brand-red: #c1272d;
    --ink: #1a1a1a;
    --tile-light: #f2f2f2;
    --tile-mid: #c9c9c9;
    --tile-side: #5f5d5e;
    --tile-edge: #8a8a8a;
  }
  * { margin: 0; padding: 0; box-sizing: border-box; }
  html, body { width: 1200px; height: 1000px; overflow: hidden; background: var(--backdrop); }
  .canvas { position: relative; width: 1200px; height: 1000px; background: var(--backdrop); }
  .poster {
    position: absolute; left: 320px; top: 113px; width: 579px; height: 823px;
    background: linear-gradient(90deg, var(--poster-yellow) 0%, var(--poster-lime) 55%, var(--poster-green) 100%);
    overflow: hidden;
  }
  .brand-mark {
    position: absolute; left: 76px; top: 48px; width: 134px; height: 134px;
    border-radius: 50%; background: var(--brand-red);
  }
  .brand-name {
    position: absolute; left: 228px; top: 72px;
    font-family: "Tinos", "Times New Roman", serif; font-weight: 700;
    font-size: 46px; line-height: 1; color: var(--brand-red);
  }
  .brand-tagline {
    position: absolute; left: 233px; top: 121px;
    font-family: "Arimo", Arial, sans-serif; font-size: 18px; line-height: 1;
    letter-spacing: 3.4px; color: var(--ink); white-space: nowrap;
  }
  .poster-title {
    position: absolute; left: 110px; top: 200px;
    font-family: "Tinos", "Times New Roman", serif; font-weight: 400;
    font-size: 55px; line-height: 1; color: var(--ink); letter-spacing: 0.5px; white-space: nowrap;
  }
  .values-board { position: absolute; left: 0; top: 0; }
  .value-label {
    font-family: "Roboto Condensed", "Arial Narrow", sans-serif; font-weight: 700;
    font-size: 24px; fill: var(--ink);
  }
</style>
</head>
<body>
<div class="canvas">
  <div class="poster">
    <div class="brand-mark"></div>
    <div class="brand-name">RWTB</div>
    <div class="brand-tagline">Learn. Grow. Together.</div>
    <h1 class="poster-title">CORE VALUES</h1>

    <svg class="values-board" width="579" height="823" viewBox="0 0 579 823" aria-label="Five core values arranged as stacked tiles">
      <defs>
        <linearGradient id="tileFace" x1="0" y1="0" x2="0" y2="1">
          <stop offset="0" stop-color="#c9c9c9"/>
          <stop offset="0.45" stop-color="#f2f2f2"/>
          <stop offset="1" stop-color="#c9c9c9"/>
        </linearGradient>
        <linearGradient id="castShadow" x1="1" y1="0" x2="0" y2="1">
          <stop offset="0" stop-color="#8a8a3a" stop-opacity="0.55"/>
          <stop offset="1" stop-color="#8a8a3a" stop-opacity="0"/>
        </linearGradient>
      </defs>

      <polygon class="cast-shadow" points="170,600 20,640 10,700 150,780 250,770" fill="url(#castShadow)"/>

      <g class="tile-sides" fill="var(--tile-side)">
        <rect x="290" y="320" width="40" height="150"/>
        <rect x="135" y="470" width="40" height="160"/>
        <rect x="130" y="610" width="40" height="160"/>
        <rect x="485" y="470" width="30" height="150"/>
      </g>

      <g class="tiles" fill="url(#tileFace)" stroke="var(--tile-edge)" stroke-width="2">
        <rect class="tile tile--customers" x="325" y="299" width="160" height="153" rx="6"/>
        <rect class="tile tile--education" x="170" y="452" width="160" height="155" rx="6"/>
        <rect class="tile tile--loyalty" x="330" y="452" width="155" height="155" rx="6"/>
        <rect class="tile tile--quality" x="170" y="607" width="160" height="155" rx="6"/>
        <rect class="tile tile--respect" x="325" y="607" width="160" height="155" rx="6"/>
      </g>

      <g class="value-labels" text-anchor="middle">
        <text class="value-label" x="405" y="344">Customers</text>
        <text class="value-label" x="405" y="381">1st</text>
        <text class="value-label" x="253" y="497">Education</text>
        <text class="value-label" x="404" y="534">Loyalty</text>
        <text class="value-label" x="252" y="693">Quality</text>
        <text class="value-label" x="409" y="657">Respect</text>
      </g>
    </svg>
  </div>
</div>
</body>
</html>
```